Brisk Harbor Funding - Letterhead

We need letterhead options for our case funding company called Brisk Harbor Funding. Here are some of the details:

Name - Brisk Harbor Funding
Phone - (555) 214 - 9083
Address - 38 Larkmoor Avenue
Suite 412
New York, NY 10958
Website - briskharborfunding.example

```html
<!DOCTYPE html>
<html lang="en">
<head>
<meta charset="utf-8">
<title>Brisk Harbor Funding – Letterhead</title>
<link rel="stylesheet" href="https://fonts.googleapis.com/css2?family=Open+Sans:wght@400;600&family=Lato:wght@400&family=Montserrat:wght@600&display=swap">
<style>
  :root {
    --backdrop: #e4e5e7;
    --paper: #ffffff;
    --navy: #1d3549;
    --body-text: #555a60;
    --footer-text: #2c3036;
    --rule: #9aa0a6;
  }
  * { box-sizing: border-box; margin: 0; padding: 0; }
  html, body { width: 1040px; height: 1200px; overflow: hidden; background: var(--backdrop); }
  .letterhead {
    position: absolute; left: 54px; top: 0;
    width: 932px; height: 1200px;
    background: var(--paper);
    font-family: "Open Sans", sans-serif;
    color: var(--body-text);
  }
  .brand {
    position: absolute; left: 0; right: 0; top: 50px;
    display: flex; justify-content: center; align-items: center; gap: 14px;
  }
  .brand-dot { width: 56px; height: 56px; border-radius: 50%; background: var(--navy); }
  .brand-name {
    font-family: "Open Sans", sans-serif; font-weight: 600;
    color: var(--navy); font-size: 17px; line-height: 19px; letter-spacing: 2px;
    text-transform: uppercase;
  }
  .letter { position: absolute; left: 87px; width: 753px; font-size: 15px; }
  .issue-date { top: 213px; }
  .recipient { top: 250px; line-height: 18px; }
  .salutation { top: 354px; }
  .body-copy { top: 410px; }
  .body-copy p { line-height: 27px; text-align: justify; margin-bottom: 27px; font-size: 14.5px; }
  .closing { top: 812px; }
  .signatory { top: 890px; }
  .signatory-name { font-size: 19px; font-weight: 600; color: #3a3f45; }
  .signatory-title { font-size: 15px; margin-top: 6px; }
  .contact-bar {
    position: absolute; left: 0; right: 0; top: 1090px;
    font-family: "Lato", sans-serif; color: var(--footer-text); font-size: 18px;
  }
  .contact-item { position: absolute; top: 0; transform: translateX(-50%); text-align: center; white-space: nowrap; }
  .contact-item svg { display: block; margin: 0 auto 12px; }
  .contact-item.phone { left: 158px; }
  .contact-item.web { left: 406px; }
  .contact-item.address { left: 713px; line-height: 22px; }
  .contact-item.phone span, .contact-item.web span { display: block; padding-top: 22px; }
  .contact-item.address svg { margin-bottom: 4px; }
  .divider { position: absolute; top: 1088px; width: 1px; height: 78px; background: var(--rule); }
  .divider.first { left: 255px; }
  .divider.second { left: 559px; }
</style>
</head>
<body>
<main class="letterhead">
  <header class="brand">
    <div class="brand-dot"></div>
    <div class="brand-name">Brisk<br>Harbor<br>Funding</div>
  </header>

  <p class="letter issue-date">Issuing Date: May 5, 2018</p>
  <p class="letter recipient">Name Of Employee Mr. XYZABC<br>Address of Employee<br>Address Line 2 etc..</p>
  <p class="letter salutation">Dear Mr.XYZABC</p>

  <section class="letter body-copy">
    <p>Lorem Ipsum has been the industry's standard dummy text ever since the 1500s, when an unknown printer took a galley of type and scrambled it to make a type specimen book. It has survived not only five centuries, but also the leap into electronic typesetting, remaining essentially unchanged. It was popularised in the 1960s with the release of Quillset sheets containing Lorem Ipsum passages, and more recently with desktop publishing software like Ardent PageForge including versions of Lorem Ipsum.</p>
    <p>Lorem Ipsum is simply dummy text of the printing and typesetting industry. Lorem Ipsum has been the industry's standard dummy text ever since the 1500s, when an unknown printer took a galley of type and scrambled it to make a type specimen book.</p>
    <p>It has survived not only five centuries, but also the leap into electronic typesetting, remaining essentially unchanged. It was popularised in the 1960s with the release of Quillset sheets containing Lorem IpsumIpsum passages.</p>
  </section>

  <p class="letter closing">Yours Sincerely</p>
  <div class="letter signatory">
    <p class="signatory-name">Marlon Teague</p>
    <p class="signatory-title">Managing Director</p>
  </div>

  <footer class="contact-bar">
    <div class="contact-item phone">
      <svg width="32" height="32" viewBox="0 0 32 32" aria-hidden="true">
        <circle cx="16" cy="16" r="14" fill="none" stroke="var(--navy)" stroke-width="2.5"/>
        <path d="M11.5 9.5l2.5-.5 1.5 3.5-1.8 1.2c.8 1.8 2.2 3.2 4 4l1.2-1.8 3.5 1.5-.5 2.5c-5 .6-10.8-5.2-10.4-10.4z" fill="var(--navy)"/>
      </svg>
      <span>(555) 214 - 9083</span>
    </div>
    <div class="contact-item web">
      <svg width="32" height="32" viewBox="0 0 32 32" aria-hidden="true">
        <circle cx="16" cy="16" r="14" fill="none" stroke="var(--navy)" stroke-width="2.5"/>
        <circle cx="16" cy="16" r="8" fill="var(--navy)"/>
        <path d="M12 13c2 0 2 2 4 2s1 3 3 3M18 10c0 2 2 2 3 3" stroke="#fff" stroke-width="1.4" fill="none"/>
      </svg>
      <span>www.briskharborfunding.example</span>
    </div>
    <div class="contact-item address">
      <svg width="32" height="32" viewBox="0 0 32 32" aria-hidden="true">
        <circle cx="16" cy="16" r="14" fill="none" stroke="var(--navy)" stroke-width="2.5"/>
        <path d="M16 25c-4-5-6-8-6-11a6 6 0 0112 0c0 3-2 6-6 11z" fill="var(--navy)"/>
        <circle cx="16" cy="14" r="2.2" fill="#fff"/>
      </svg>
      38 Larkmoor Avenue<br>Suite 412 New York, NY 10958
    </div>
  </footer>
  <div class="divider first"></div>
  <div class="divider second"></div>
</main>
</body>
</html>
```